Wine Bottle Label Logo Design

My fiancé and I are getting married in September and we made homemade wine which will be given to the guests as a wedding favor. We need label/logo for our wine bottles. We were looking for something rustic yet modern and simple. We had an idea for beige and cranberry colored wine stained, weathered, imperfect heart. Things that will need to be incorporated into the label design are as follows:
Our last name and also the name of the wine: Bastoni
The year: 2012
Where is says Alcohol Content on a wine bottle normally write: Alcohol: Deceiving% by vol.
Type of wine: Red Wine
Incorporate our wedding date: Foot Stomped and Bottled for Jess and Ned's Wedding Day 9/28/13

```html
<!DOCTYPE html>
<html lang="en">
<head>
<meta charset="utf-8">
<title>Bastoni Wine Label</title>
<link rel="stylesheet" href="https://fonts.googleapis.com/css2?family=Nothing+You+Could+Do&family=Over+the+Rainbow&display=swap">
<style>
  :root {
    --wood-light: #dcd7cf;
    --wood-mid: #cbc5bc;
    --wood-dark: #b9b2a8;
    --heart-top: #8c5f63;
    --heart-bottom: #7a4b50;
    --name-white: #ffffff;
    --year-ink: #1f1a1a;
    --caption-ink: #5b3a3f;
    --heart-icon: #7a4d55;
  }
  html, body {
    margin: 0;
    padding: 0;
    width: 960px;
    height: 1200px;
    overflow: hidden;
  }
  .label {
    position: relative;
    width: 960px;
    height: 1200px;
    overflow: hidden;
  }
  .wood-backdrop {
    position: absolute;
    inset: 0;
    background: linear-gradient(90deg, var(--wood-mid) 0%, var(--wood-light) 30%, var(--wood-mid) 55%, var(--wood-light) 80%, var(--wood-dark) 100%);
  }
  .heart {
    position: absolute;
    left: 0;
    top: 0;
    width: 960px;
    height: 1200px;
  }
  .family-name {
    position: absolute;
    left: 0;
    width: 960px;
    top: 150px;
    text-align: center;
    font-family: "Over the Rainbow", cursive;
    font-size: 280px;
    line-height: 1;
    color: var(--name-white);
    letter-spacing: -6px;
  }
  .vintage-year {
    position: absolute;
    left: 0;
    width: 960px;
    top: 755px;
    text-align: center;
    font-family: "Over the Rainbow", cursive;
    font-size: 86px;
    line-height: 1;
    color: var(--year-ink);
    letter-spacing: 8px;
  }
  .dedication {
    position: absolute;
    left: 0;
    width: 960px;
    text-align: center;
    font-family: "Nothing You Could Do", cursive;
    font-size: 42px;
    line-height: 1;
    color: var(--caption-ink);
    letter-spacing: 4px;
  }
  .dedication-first { top: 968px; }
  .dedication-second {
    top: 1048px;
    display: flex;
    justify-content: center;
    align-items: center;
    gap: 24px;
  }
  .heart-icon { width: 56px; height: 50px; }
</style>
</head>
<body>
  <main class="label">
    <div class="wood-backdrop" role="img" aria-label="Weathered grey-beige wooden plank texture"></div>

    <svg class="heart" viewBox="0 0 960 1200" aria-hidden="true">
      <defs>
        <linearGradient id="heartWash" x1="0" y1="0" x2="0" y2="1">
          <stop offset="0" stop-color="var(--heart-top)"/>
          <stop offset="1" stop-color="var(--heart-bottom)"/>
        </linearGradient>
      </defs>
      <path fill="url(#heartWash)" d="M483 172 C 430 62, 300 30, 218 60 C 128 95, 104 205, 128 305 C 165 445, 330 565, 485 738 C 640 565, 805 445, 840 305 C 866 195, 832 78, 740 52 C 650 28, 530 62, 483 172 Z"/>
    </svg>

    <h1 class="family-name" style="margin:0;font-weight:400;">bastoni</h1>
    <p class="vintage-year" style="margin:0;">2012</p>

    <p class="dedication dedication-first" style="margin:0;">Made with love for Jess and Ned's</p>
    <p class="dedication dedication-second" style="margin:0;">
      <span>Wedding Day</span>
      <svg class="heart-icon" viewBox="0 0 56 50" aria-hidden="true">
        <path fill="var(--heart-icon)" d="M28 12 C 22 0, 2 0, 2 16 C 2 30, 20 40, 28 50 C 36 40, 54 30, 54 16 C 54 0, 34 0, 28 12 Z"/>
      </svg>
      <span>09.28.13</span>
    </p>
  </main>
</body>
</html>
```